Business Card Design Project

Thornwick Property Management

Our Business is residential property management, we therefore need a card that displays a professional image, but is clear and concise, and easy to read
Updates

We are committed now guys and girls, loving what we are seeing so far! 

Target Market(s)

Landlords, Rental Property Owners

Industry/Entity Type

Residential

Requirements
Must have
• Dale Thornwick - Principal
Fiona Thornwick - Director (Property Management)

PO Box 817
Pellworth SA 5193

Dale: 0490 367 258
Fiona: 0490 723 519

www.thornwickpropertymanagement.com.au
admin@thornwickpropertymanagement.com.au

Nice to have
• I would like the card to be double sided, white background on the information side and then colour on the reverse, in blue or black and incorporating our logo

```html
<!DOCTYPE html>
<html lang="en">
<head>
<meta charset="utf-8">
<title>Thornwick Property Management – Business Card</title>
<link rel="stylesheet" href="https://fonts.googleapis.com/css2?family=Open+Sans:ital,wght@0,400;0,600;0,700;1,700&display=swap">
<style>
  :root {
    --stage: #e8e5e1;
    --card-white: #ffffff;
    --brand-blue: #1a6db5;
    --brand-blue-soft: #4b8fc7;
    --text-grey: #6b6b6b;
    --text-dark: #3d3d3d;
    --mark-dark: #121417;
    --bullet-grey: #5c5c5c;
    --reverse-start: #4a90c9;
    --reverse-mid: #4c86b8;
    --reverse-end: #5e6770;
  }
  * { margin: 0; padding: 0; box-sizing: border-box; }
  html, body {
    width: 1200px; height: 750px; overflow: hidden;
    background: var(--stage);
    font-family: "Open Sans", Arial, sans-serif;
  }
  .canvas { position: relative; width: 1200px; height: 750px; }

  .card {
    position: absolute; top: 200px; width: 491px; height: 353px;
    box-shadow: 0 2px 6px rgba(0,0,0,0.18);
  }
  .card--front { left: 85px; background: var(--card-white); }
  .card--back {
    left: 640px;
    background: linear-gradient(135deg, var(--reverse-start) 0%, var(--reverse-mid) 45%, var(--reverse-end) 100%);
  }

  .abs { position: absolute; white-space: nowrap; }

  /* Front wordmark */
  .wordmark-square { left: 30px; top: 34px; width: 46px; height: 46px; background: var(--brand-blue); }
  .wordmark { left: 88px; top: 22px; color: var(--text-dark); font-weight: 600; line-height: 1; }
  .wordmark__name { display: block; font-size: 44px; letter-spacing: -0.5px; }
  .wordmark__sub { display: block; font-size: 15px; margin-top: 6px; }

  /* Contact block */
  .bullet { width: 11px; height: 11px; background: var(--bullet-grey); }
  .person-name { color: var(--brand-blue); font-weight: 700; font-style: italic; font-size: 22px; }
  .person-role { color: var(--text-grey); font-size: 19px; font-weight: 400; }
  .person-role small { font-size: 11px; }
  .line-blue { color: var(--brand-blue); font-size: 18px; font-weight: 600; }
  .phone-label { color: var(--brand-blue); font-weight: 600; }
  .phone-number { color: var(--text-grey); font-weight: 400; }
  .web-line { color: var(--text-dark); font-size: 16.5px; font-weight: 600; }

  /* Reverse wordmark */
  .reverse-square { left: 65px; top: 148px; width: 46px; height: 46px; background: var(--card-white); }
  .reverse-wordmark { left: 124px; top: 128px; color: var(--mark-dark); font-weight: 700; line-height: 1; }
  .reverse-wordmark__name { display: block; font-size: 58px; letter-spacing: -1px; }
  .reverse-wordmark__sub { display: block; font-size: 17px; margin-top: 6px; padding-left: 40px; }
</style>
</head>
<body>
<main class="canvas">

  <section class="card card--front" aria-label="Information side">
    <div class="abs wordmark-square"></div>
    <div class="abs wordmark">
      <span class="wordmark__name">Thornwick</span>
      <span class="wordmark__sub">Property Management</span>
    </div>

    <div class="abs bullet" style="left:28px; top:131px;"></div>
    <p class="abs" style="left:47px; top:121px;">
      <span class="person-name">Dale Thornwick</span>
      <span class="person-role">Principal</span>
    </p>
    <p class="abs" style="left:42px; top:148px;">
      <span class="person-name">Fiona Thornwick</span>
      <span class="person-role">Director <small>(Property Management)</small></span>
    </p>

    <div class="abs bullet" style="left:28px; top:183px;"></div>
    <p class="abs line-blue" style="left:45px; top:174px;">PO Box 817</p>
    <p class="abs line-blue" style="left:46px; top:200px;">Pellworth SA 5193</p>

    <div class="abs bullet" style="left:28px; top:233px;"></div>
    <p class="abs line-blue" style="left:43px; top:224px;">
      <span class="phone-label">Dale:</span> <span class="phone-number">0490 367 258</span>
    </p>
    <p class="abs line-blue" style="left:43px; top:254px;">
      <span class="phone-label">Fiona:</span> <span class="phone-number">0490 723 519</span>
    </p>

    <p class="abs web-line" style="left:23px; top:283px;">www.thornwickpropertymanagement.com.au</p>
    <p class="abs web-line" style="left:23px; top:309px;">admin@thornwickpropertymanagement.com.au</p>
  </section>

  <section class="card card--back" aria-label="Logo side">
    <div class="abs reverse-square"></div>
    <div class="abs reverse-wordmark">
      <span class="reverse-wordmark__name">Thornwick</span>
      <span class="reverse-wordmark__sub">Property Management</span>
    </div>
  </section>

</main>
</body>
</html>
```